Vocational Mentor needs an impressive business card

1. I need a business card (or maybe three with identic look) to promote me and my three business titles/services:
- Vocational Mentor. I help people find their vocation and live happily from it. I use my 20 years of experience in business, management and psychology to help them identify the most efficient ways to make a living doing what they are passionate about.
- Business Angel. I help founders start a succesful business with minimum risks and costs. I use my 20 years of experience in sales, management and entrepreneurship to help them identify the most efficient ways, in terms of time and cost, to validate their business idea.
- Learning Designer. I design unique learning programs that produce long-term cognitive and behavioural changes to people and organisations. I use my 20 years of experience in learning, teaching and change management to create minimalist experiences and processes that allow them to change efficiently in their pursued direction.

2. I would like a two-sided business card, on the front with my name, contact details and titles, on the back the explanation of the services.
Updates

Hi all,

I updated my brief, included contacts info and give feedback on all designs I got. I am new on this platform so please tell me if you need anything else or if I don't use corectly the platform forms.

Kind regards,
Tudor

Hi all,

I shortened the services description by deleting the phrase "I call..."

Kind regards,
Tudor

Target Market(s)

Freelancers, startups, people and organization willing to invest in change through ultimate learning experiences

Industry/Entity Type

Business

Font styles to use
Serif

Requirements
Must have
• Front side: full name, titles, web site, email, phone like below:
Tudor Vasilache
Vocational Mentor, Business Angel, Learning Designer
info@tudorvasilache.example
www.tudorvasilache.example
+40-745-TUDORV
Nice to have
• Back side: the description of the services I provide as in the task description.
1/3: it would be nice if I can jam all three titles on the front side but then I need a solution to jam all three services on the back side.

```html
<!DOCTYPE html>
<html lang="en">
<head>
<meta charset="utf-8">
<title>Tudor Vasilache – Business Card</title>
<link href="https://fonts.googleapis.com/css2?family=Roboto+Slab:wght@300;400;700&family=Varela+Round&display=swap" rel="stylesheet">
<style>
  :root {
    --backdrop: #6b8fa3;
    --card: #06172f;
    --band-green: #9ccf80;
    --name-ink: #0b2238;
    --mentor-blue: #3aa3dc;
    --angel-green: #9ccf80;
    --designer-sky: #8fd3ec;
    --mentor-bar: #1f7fc0;
    --angel-bar: #6fae5c;
    --designer-bar: #4f9ea6;
    --mentor-text: #3a92d2;
    --angel-text: #7fbd6c;
    --designer-text: #62afb6;
  }
  * { box-sizing: border-box; margin: 0; padding: 0; }
  html, body { width: 1200px; height: 900px; overflow: hidden; }
  body {
    position: relative;
    background: var(--backdrop);
    font-family: "Roboto Slab", "Rockwell", serif;
  }
  .card {
    position: absolute;
    width: 514px;
    height: 289px;
    background: var(--card);
    box-shadow: 8px 14px 22px rgba(20, 40, 60, 0.35);
  }
  .card--front {
    left: 185px; top: 118px;
    font-family: "Varela Round", "Trebuchet MS", sans-serif;
  }
  .card--back { left: 501px; top: 501px; }

  .name-band {
    position: absolute;
    left: 0; right: 0;
    top: 25px;
    height: 60px;
    border-top: 3px solid var(--band-green);
    border-bottom: 3px solid var(--band-green);
  }
  .name-band__fill {
    position: absolute;
    left: 0; right: 0; top: 3px; bottom: 3px;
    background: var(--band-green);
    display: flex; align-items: center; justify-content: center;
  }
  .name {
    font-weight: 400;
    font-size: 26px;
    color: var(--name-ink);
    letter-spacing: 0.2px;
  }
  .titles {
    position: absolute;
    top: 99px; left: 0; right: 0;
    text-align: center;
    font-weight: 400;
    font-size: 17px;
    line-height: 23.5px;
  }
  .titles .mentor { color: var(--mentor-blue); }
  .titles .angel { color: var(--angel-green); }
  .titles .designer { color: var(--designer-sky); }
  .divider {
    position: absolute;
    left: 118px; top: 187px;
    width: 277px; height: 3px;
    border-radius: 2px;
    background: linear-gradient(90deg, rgba(156,207,128,0.35), var(--band-green) 35%, var(--band-green) 65%, rgba(156,207,128,0.35));
  }
  .contacts {
    position: absolute;
    top: 209px; left: 0; right: 0;
    text-align: center;
    font-weight: 400;
    font-size: 15px;
    line-height: 21px;
    color: var(--angel-green);
  }

  .services {
    position: absolute;
    left: 25px; top: 25px;
    width: 469px;
  }
  .service {
    border-left: 3px solid;
    padding-left: 7px;
    font-weight: 300;
    font-size: 13px;
    line-height: 16.4px;
    text-align: justify;
    hyphens: auto;
    margin-bottom: 14px;
  }
  .service strong { font-weight: 700; }
  .service--mentor { border-color: var(--mentor-bar); color: var(--mentor-text); }
  .service--mentor strong { color: var(--mentor-blue); }
  .service--angel { border-color: var(--angel-bar); color: var(--angel-text); }
  .service--angel strong { color: var(--angel-green); }
  .service--designer { border-color: var(--designer-bar); color: var(--designer-text); }
  .service--designer strong { color: var(--designer-sky); }
</style>
</head>
<body>
  <section class="card card--front">
    <div class="name-band">
      <div class="name-band__fill"><h1 class="name">Tudor Vasilache</h1></div>
    </div>
    <div class="titles">
      <div class="mentor">Vocational Mentor</div>
      <div class="angel">Business Angel</div>
      <div class="designer">Learning Designer</div>
    </div>
    <div class="divider" role="img" aria-label="Decorative divider ornament between titles and contact details"></div>
    <div class="contacts">
      <div class="phone">+40-745-TUDORV</div>
      <div class="email">info@tudorvasilache.example</div>
      <div class="web">www.tudorvasilache.example</div>
    </div>
  </section>

  <section class="card card--back">
    <div class="services">
      <p class="service service--mentor"><strong>Vocational Mentor.</strong> I help people find their vocation and live happily from it. I use my 20 years of experience in business, management and psychology to help you identify the most efficient ways to make a living doing what you are passionate about.</p>
      <p class="service service--angel"><strong>Business Angel.</strong> I help founders start a successful business with minimum risks and costs. I use my 20 years of experience in sales, management and entrepreneurship to help you identify the most efficient ways, in terms of time and cost, to validate your business idea.</p>
      <p class="service service--designer"><strong>Learning Designer.</strong> I design unique learning programs that produce long-term cognitive and behavioural changes to people and organisations. I use my 20 years of experience in learning, teaching and change management to create minimalist experiences and processes that allow you to change efficiently in your pursued direction.</p>
    </div>
  </section>
</body>
</html>
```